Flyer Design Print Ad for Clothing Store

We are a modest women's clothing store. We are looking for a print ad 90*134 mm that is attention grabbing and can serve as a template for us going forward. We cannot use pictures of actual women. We need it to include our logo, store hours, physical address, website, phone number. We would use this template and change the call to action as necessary e. g. BOGO Sale, 30% off, flash sale, summer sale etc. Our colors are black and white and our fonts are Bodoni sans and Athens.

Target Market(s)

Women from teen to age 70

Industry/Entity Type

Women's clothing

Font styles to use
Other font styles liked:
• Athens, Bodoni Sans

Requirements
Must have
• Our, logo, phone number, website, address and store hours
Nice to have
• I'd like something that's not just our flat logo but something that will make someone pause to look
Should not have
• Pictures of women

```html
<!DOCTYPE html>
<html lang="en">
<head>
<meta charset="utf-8">
<title>Modestine – BOGO Sale Print Ad</title>
<link rel="stylesheet" href="https://fonts.googleapis.com/css2?family=Marcellus&family=Noto+Sans+Hebrew:wght@300;400;600&family=Open+Sans:wght@600;700&family=Roboto+Condensed:wght@600&display=swap">
<style>
  :root {
    --ink: #111a22;
    --band-dark: #111418;
    --band-mid: #2a2e33;
    --paper-light: #efe7da;
    --paper-mid: #e2d6c4;
    --paper-deep: #cfc0a8;
    --stroke-cream: #f6f0e4;
    --white: #ffffff;
    --stage: #f1f1f1;
  }
  * { margin: 0; padding: 0; box-sizing: border-box; }
  html, body { width: 720px; height: 1200px; overflow: hidden; background: var(--stage); }
  .stage { position: relative; width: 720px; height: 1200px; }

  .flyer {
    position: absolute; left: 0; top: 64px; width: 720px; height: 1072px;
    overflow: hidden;
    background: radial-gradient(ellipse at 55% 40%, var(--paper-light) 0%, var(--paper-mid) 70%, var(--paper-deep) 100%);
    color: var(--ink);
  }

  .paper-motif {
    position: absolute; left: 60px; top: 0; width: 640px; height: 900px;
    background: radial-gradient(ellipse at 50% 55%, rgba(255,255,255,0.35) 0%, rgba(255,255,255,0) 65%);
  }
  .pattern-disc {
    position: absolute; left: -160px; top: 635px; width: 320px; height: 330px;
    border-radius: 50%;
    background: radial-gradient(circle at 60% 50%, #d6cab8 0%, #c9bba4 100%);
  }
  .brush-stroke {
    position: absolute; left: 0; top: 395px; width: 640px; height: 170px;
    border-radius: 50% 60% 40% 50%;
    background: linear-gradient(100deg, rgba(246,240,228,0.9) 0%, rgba(246,240,228,0.6) 55%, rgba(246,240,228,0) 100%);
    transform: rotate(-6deg);
  }

  .brand {
    position: absolute; left: 47px; top: 140px; width: 225px;
    font-family: "Marcellus", serif; font-size: 27px; letter-spacing: 5px;
    text-align: center; color: var(--ink);
  }

  .hours-band { position: absolute; left: 388px; top: 66px; width: 332px; height: 58px; }
  .hours-text {
    position: absolute; left: 410px; top: 70px; width: 300px;
    font-family: "Roboto Condensed", sans-serif; font-weight: 600;
    font-size: 20px; line-height: 24px; color: var(--white); text-align: center;
  }

  .headline {
    position: absolute; left: 0; top: 345px; width: 720px; text-align: center;
    font-family: "Marcellus", serif; font-size: 112px; line-height: 1; color: var(--ink);
  }
  .offer {
    position: absolute; left: 0; top: 462px; width: 720px; text-align: center;
    font-family: "Marcellus", serif; font-size: 92px; line-height: 1; color: var(--ink);
  }
  .offer sup { font-size: 44px; vertical-align: 38px; margin-left: 2px; }

  .location { position: absolute; left: 110px; top: 733px; width: 540px; text-align: center; }
  .location .he-name {
    font-family: "Noto Sans Hebrew", sans-serif; font-weight: 300;
    font-size: 35px; line-height: 46px;
  }
  .location .en-name {
    font-family: "Open Sans", sans-serif; font-weight: 700;
    font-size: 25px; line-height: 38px;
  }
  .location .he-note {
    font-family: "Noto Sans Hebrew", sans-serif; font-weight: 400;
    font-size: 19px; line-height: 34px;
  }
  .location .he-street {
    font-family: "Noto Sans Hebrew", sans-serif; font-weight: 400;
    font-size: 17px; line-height: 30px;
  }
  .location .he-street b { font-family: "Open Sans", sans-serif; font-weight: 700; }
  .location .buses {
    font-family: "Open Sans", sans-serif; font-weight: 700;
    font-size: 16px; line-height: 30px;
  }

  .phone-band {
    position: absolute; left: 0; top: 960px; width: 720px; height: 64px;
    background: var(--band-dark); color: var(--white); text-align: center;
    font-family: "Marcellus", serif; font-size: 48px; line-height: 64px; letter-spacing: 5px;
  }
  .web-band {
    position: absolute; left: 0; top: 1024px; width: 720px; height: 48px;
    background: var(--band-mid); color: #ececec; text-align: center;
    font-family: "Marcellus", serif; font-size: 25px; line-height: 48px; letter-spacing: 5px;
  }
</style>
</head>
<body>
<div class="stage">
  <main class="flyer">
    <div class="paper-motif" role="img" aria-label="Faint floral ornament and damask pattern on beige paper texture"></div>
    <div class="pattern-disc" role="img" aria-label="Circular panel of small damask pattern"></div>
    <div class="brush-stroke" role="img" aria-label="Cream paint brush stroke behind the headline"></div>

    <div class="brand">MODESTINE</div>

    <svg class="hours-band" viewBox="0 0 332 58" aria-hidden="true">
      <polygon points="30,0 332,0 332,58 0,58" fill="#111418"/>
    </svg>
    <div class="hours-text">
      <div>S-Th - 10:30-12:30 <span lang="he">א-ה</span></div>
      <div>20:30 - 22:30</div>
    </div>

    <h1 class="headline">BOGO SALE</h1>
    <p class="offer">30%<sup>OFF</sup></p>

    <address class="location" style="font-style: normal;">
      <div class="he-name" lang="he" dir="rtl">מרכז מסחרי גבעת ארזים</div>
      <div class="en-name">Cedar Hill Shopping Center</div>
      <div class="he-note" lang="he" dir="rtl">(מעל המאפייה)</div>
      <div class="he-street" lang="he" dir="rtl">ניתן להגיע גם משדרות הארזים <b>16</b></div>
      <div class="buses">Buses 21, 22, 39, 41, 45, 52, 59, 65, 68, 69, 77</div>
    </address>

    <div class="phone-band">077-5550142</div>
    <div class="web-band">www.modestine.co.il</div>
  </main>
</div>
</body>
</html>
```